physio rehab flyer for Vela Motion please

Specification:
Flyer is to be trifold from letter size (8.5 x 11)
-----------------------This may help you:--------------------------
I would like the look of :
clean, minimalistic look with mainly blue and green
san serif font
professional
The colors I like are blue (not the blue in the logo enclosed, I want a change, but more like the blue on my website logo) and light green.
This is my website: www.velamotiongroup.ca just so you get an idea but it will be totally changed soon to a to be determined design.
I like the blue and green in file "sample 2" (enclosed)
I like the pictures in "sample 2" file enclosed
For inspiration, I like design of this brochure: http://www.qlx.ca/HarbourRestore/PatientsFamilies/Clinics_Tests/DAWL_Service/Documents/Brochure.pdf
Here's how I see the pages layout:
----[location: this should be the cover (outside, right panel of trifold)]-----
Vela Motion Logo
Integrated Injury Rehab
Evidence-based, one-on-one care to make your recovery fast and comfortable
www.velamotiongroup.ca
---------------[location: inside, left panel]----------------------------------------
Our team leaders
[portrait here]
Harriet Osei, MD, FRCPC, MSC, CIME
Physiatrist
Dr. Osei specializes in injury rehab and sports medicine. She is highly trained having received her MD and Residency in Physiatry from Wexmoor University. Her passion is to help injured people get back to their life.
[portrait here]
Dorothy Varga, PT
Physiotherapist
Dorothy has over 10 years of experience as a Physiotherapist (5 in Canada). She has advanced training in orthopedics and manual therapy. She loves and relates well with people from the youngest to the most senior.
--------------------[location: inside, middle panel]-------------------------------
Our services
We provide integrated assessment and care from interprofessional team of regulated healthcare professionals with proven experience in injury rehabilitation:
physiatrists
sport medicine physicians
physiotherapists
chiropractors
massage therapists
acupuncturists
psychologists
We provide custom medical bracing, orthotics, orthopedic shoes, assistive devices, and medical stockings, all in one place.
----------------------[location: inside, right panel]-----------------------------------
Only registered physiotherapists
We strongly believe in consistency with your treatment plan. This means that you spend your time here one-on-one with your physiotherapist, not any students or assistants. You get consistent high quality care from a professional.
One-on-one attention
We book maximum 3 people per hour to ensure everyone gets adequate one-on-one time with their physiotherapist. This compares favorably with other clinics, who may book upwards of 5-6 per hour. The atmosphere is professional -balanced with friendly, caring and relaxed. Our highly qualified staff operate this way to help make your recovery faster and more enjoyable.
------------------------[location: outside, left panel]---------------------------------
The right rehab for your clients
Timely access to comprehensive assessment and treatment
Proven track record in injury rehabilitation
Convenient one-stop service
Customized treatment plans
Integrated, co-ordinated care
Evidence-based care applying leading best practices
Access to specialty clinics: Physiatry and Chronic Pain
-------------------------[location: outside, middle panel]--------------------------
Please call us 416-738-4062
for more information on injury rehabilitation
Vela Motion Group
8120 Tolliver Rd., Unit 9
Scarborough, ON M4K 8B2
[Please include a line art map designed based on "map" file enclosed]
To make a referral for your clients, contact velamotiongroup@brisklane.ca or fax: 416-738-4059. Thank you.
www.velamotiongroup.ca
------------------------------------------------------------------------------------------------
Target Market(s)
family doctors, ER docs, lawyers, and general public age (20-50)
Industry/Entity Type
Health And Wellness
Requirements
Must have
- san serif font
- blue and green colors
- clean, sophisticated look
Nice to have
- consumer choice award badge either on front or back of trifold
Should not have
- see above

```html
<!DOCTYPE html>
<html lang="en">
<head>
<meta charset="utf-8">
<title>Vela Motion – Integrated Injury Rehab Trifold</title>
<link rel="stylesheet" href="https://fonts.googleapis.com/css2?family=Ubuntu:wght@400;500;700&family=Open+Sans:wght@400;600;700&display=swap">
<style>
  :root{
    --stage:#a7a8aa;
    --paper:#ffffff;
    --panel-grey:#f3f4f4;
    --blue:#2f6db4;
    --blue-soft:#5b86c0;
    --blue-bar:#5d8cc6;
    --blue-column:#8eb0dd;
    --green:#8cc63f;
    --green-light:#c4e07a;
    --ink:#3b3b3b;
    --photo-skin:#d9b9a0;
    --photo-blue:#9cc0e6;
  }
  *{margin:0;padding:0;box-sizing:border-box}
  html,body{width:840px;height:1200px;overflow:hidden}
  body{background:var(--stage);position:relative;font-family:"Open Sans",Arial,sans-serif;color:var(--ink)}
  .sheet{position:absolute;left:33px;width:777px;background:var(--paper);box-shadow:2px 3px 8px rgba(0,0,0,.35);overflow:hidden}
  .sheet--outside{top:33px;height:547px}
  .sheet--inside{top:612px;height:553px}
  .abs{position:absolute}
  .heading{font-family:"Ubuntu",Arial,sans-serif;font-weight:700;text-transform:uppercase;line-height:1.28}

  /* outside left */
  .panel-referral{left:0;top:0;width:259px;height:547px}
  .panel-referral .heading{left:27px;top:22px;font-size:27.5px;color:var(--blue);line-height:39px}
  .benefits{left:30px;top:152px;width:205px;list-style:none}
  .benefits li{position:relative;padding-left:14px;font-size:12px;line-height:16px;color:var(--blue);margin-bottom:15.5px}
  .benefits li::before{content:"";position:absolute;left:0;top:6px;width:5px;height:5px;border-radius:50%;background:var(--green)}

  /* outside middle */
  .panel-contact{left:259px;top:0;width:258px;height:547px;text-align:center;border-left:1px solid #eee}
  .panel-contact .heading{left:0;width:100%;top:30px;font-size:28px;color:var(--blue)}
  .contact-block{left:0;width:100%;font-size:9.6px;font-weight:700;text-transform:uppercase;line-height:13.4px;color:var(--ink)}
  .contact-block .phone{display:block;font-size:18px;color:var(--green);font-weight:600;line-height:24px}
  .contact-block .blue,.contact-block.blue{color:var(--blue)}
  .contact-block.green{color:var(--green);letter-spacing:1px}
  .map{left:53px;top:340px;width:153px;height:119px;background:#e7ecf5;border:2px solid #2b3a85}

  /* outside right: cover */
  .panel-cover{left:517px;top:0;width:260px;height:547px}
  .cover-brand{left:0;top:0;width:260px;height:282px;background:var(--panel-grey)}
  .brand-name{left:0;top:62px;width:260px;text-align:center;font-family:"Ubuntu",Arial,sans-serif;font-weight:700;font-size:44px;line-height:50px;color:var(--blue)}
  .brand-dot{left:112px;top:28px;width:36px;height:36px;border-radius:50%;background:var(--blue)}
  .cover-line{left:0;top:210px;width:260px;text-align:center;font-family:"Ubuntu",Arial,sans-serif;font-size:14.5px;color:var(--green);text-transform:uppercase}
  .cover-line::before{content:"";position:absolute;left:16px;right:16px;top:-6px;border-top:1px solid var(--green)}
  .cover-tag{left:20px;top:238px;width:220px;text-align:center;font-size:8.6px;font-weight:600;color:var(--blue);text-transform:uppercase;line-height:12px}
  .cover-photo{left:0;top:282px;width:260px;height:210px;background:linear-gradient(135deg,var(--photo-blue) 0%,#f1ebe6 45%,var(--photo-skin) 100%)}
  .cover-url{left:0;top:510px;width:260px;text-align:center;font-size:11px;letter-spacing:2.6px;color:var(--blue);text-transform:uppercase}

  .wave-band{background:linear-gradient(180deg,rgba(196,224,122,0) 0%,rgba(196,224,122,.45) 40%,rgba(140,198,63,.35) 65%,rgba(196,224,122,0) 100%)}
  .waves{left:0;top:440px;width:517px;height:110px}
  .waves-inside{left:260px;top:365px;width:287px;height:95px}

  /* inside */
  .stripe{left:0;width:777px;height:12px;background:var(--green)}
  .panel-team{left:0;top:12px;width:259px;height:528px;background:var(--panel-grey)}
  .panel-team .heading{left:27px;top:28px;font-size:28px;line-height:30px}
  .panel-team .heading span{display:block}
  .t-blue{color:var(--blue-soft)}
  .t-green{color:var(--green)}
  .portrait{width:100px;height:100px;background:linear-gradient(160deg,#e9edf0,#c9a48c 60%,#8a6d85)}
  .leader-dot{width:40px;height:40px;border-radius:50%;background:var(--blue)}
  .leader-name{font-family:"Ubuntu",Arial,sans-serif;font-weight:500;font-size:12px;color:#9dbb34;text-transform:uppercase;border-bottom:1px solid var(--green);width:101px;line-height:15px}
  .leader-role{font-family:"Ubuntu",Arial,sans-serif;font-weight:700;font-size:12px;color:var(--blue);text-transform:uppercase;line-height:16px}
  .leader-creds{font-size:5.5px;color:var(--blue);letter-spacing:.3px}
  .bio{left:13px;width:219px;font-size:11.4px;line-height:16px;text-align:justify;color:#333}

  .services-bar{left:260px;top:48px;width:492px;height:91px;background:var(--blue-bar)}
  .award{left:271px;top:68px;width:52px;height:52px;border-radius:50%;background:radial-gradient(circle,#e9c56a,#b58a2a)}
  .services-title{left:339px;top:79px;font-family:"Ubuntu",Arial,sans-serif;font-weight:500;font-size:25px;color:#fff}
  .services-list{left:260px;top:172px;width:287px;list-style:none;text-align:center}
  .services-list li{font-family:"Ubuntu",Arial,sans-serif;font-weight:700;font-size:16px;line-height:24.8px;text-transform:uppercase}
  .services-list li:nth-child(odd){color:var(--green)}
  .services-list li:nth-child(even){color:var(--blue)}
  .services-note{left:314px;top:476px;width:180px;text-align:center;font-size:9.6px;line-height:13px;color:#444}

  .panel-promise{left:547px;top:12px;width:205px;height:528px;background:var(--blue-column)}
  .promise-lead{left:567px;top:59px;width:165px;text-align:center;font-size:10.4px;line-height:14px;color:#fff;font-weight:600}
  .promise-head{left:580px;width:140px;text-align:center;font-family:"Ubuntu",Arial,sans-serif;font-weight:700;font-size:14px;line-height:18px;color:var(--green-light);text-transform:uppercase}
  .promise-body{left:562px;width:175px;text-align:center;font-size:10.2px;line-height:13.6px;color:#fff;font-weight:600}
</style>
</head>
<body>

<section class="sheet sheet--outside">
  <div class="abs panel-referral">
    <h2 class="abs heading">The right<br>rehab for<br>your clients</h2>
    <ul class="abs benefits">
      <li>Timely access to comprehensive assessment and treatment</li>
      <li>Proven track record in injury rehabilitation</li>
      <li>Convenient one-stop service</li>
      <li>Customized treatment plans</li>
      <li>Integrated, co-ordinated care</li>
      <li>Evidence-based care applying leading best practices</li>
      <li>Access to specialty clinics: Physiatry and Chronic Pain</li>
    </ul>
  </div>

  <div class="abs panel-contact">
    <h2 class="abs heading">Get in touch</h2>
    <p class="abs contact-block" style="top:82px">Please call us on<span class="phone">416-738-4062</span></p>
    <p class="abs contact-block" style="top:132px">For more information on<br>injury rehabilitation, visit us:</p>
    <p class="abs contact-block blue" style="top:172px">Vela Motion Group<br>8120 Tolliver Road,<br>Unit 9, Scarborough<br>ON M4K 8B2</p>
    <p class="abs contact-block" style="top:238px">To make a referral for your<br>clients, contact<br><span class="blue">velamotiongroup@brisklane.ca</span><br>or <span class="blue">fax: 416-738-4059</span></p>
    <p class="abs contact-block green" style="top:304px">www.velamotiongroup.ca</p>
    <div class="abs map" role="img" aria-label="Line map of the streets around the clinic"></div>
  </div>

  <div class="abs wave-band waves" role="img" aria-label="Soft green flowing wave decoration"></div>

  <div class="abs panel-cover">
    <div class="abs cover-brand"></div>
    <div class="abs brand-dot"></div>
    <p class="abs brand-name">Vela<br>Motion</p>
    <p class="abs cover-line">Integrated Injury Rehab</p>
    <p class="abs cover-tag">Evidence-based, one-on-one care to make your recovery fast &amp; comfortable</p>
    <div class="abs cover-photo" role="img" aria-label="Photo of a physiotherapist treating a patient's braced knee"></div>
    <p class="abs cover-url">velamotiongroup.ca</p>
  </div>
</section>

<section class="sheet sheet--inside">
  <div class="abs stripe" style="top:0"></div>
  <div class="abs stripe" style="top:540px;height:6px"></div>

  <div class="abs panel-team">
    <h2 class="abs heading"><span class="t-blue">Our team</span><span class="t-green">leaders</span></h2>
    <div class="abs portrait" style="left:29px;top:94px" role="img" aria-label="Portrait of Harriet Osei"></div>
    <div class="abs leader-dot" style="left:157px;top:102px"></div>
    <p class="abs leader-name" style="left:139px;top:153px">Harriet Osei</p>
    <p class="abs leader-role" style="left:139px;top:170px">Physiatrist</p>
    <p class="abs leader-creds" style="left:139px;top:187px">MD . FRCPC . MSC . CIME</p>
    <p class="abs bio" style="top:204px">Dr. Osei specializes in injury rehab and sports medicine. She is highly trained having received her MD and Residency in Physiatry from Wexmoor University. Her passion is to help injured people get back to their life.</p>

    <div class="abs leader-dot" style="left:52px;top:321px"></div>
    <p class="abs leader-name" style="left:19px;top:360px;text-align:right">Dorothy Varga</p>
    <p class="abs leader-role" style="left:0;top:377px;width:120px;text-align:right">Physiotherapist</p>
    <p class="abs leader-creds" style="left:0;top:394px;width:120px;text-align:right">PT</p>
    <div class="abs portrait" style="left:130px;top:311px" role="img" aria-label="Portrait of Dorothy Varga"></div>
    <p class="abs bio" style="top:430px">Dorothy has over 10 years of experience as a Physiotherapist (5 in Canada). She has advanced training in orthopedics and manual therapy. She loves and relates well with people from the youngest to the most senior.</p>
  </div>

  <div class="abs panel-promise"></div>
  <div class="abs services-bar"></div>
  <div class="abs award" role="img" aria-label="Award badge"></div>
  <h2 class="abs services-title">OUR SERVICES</h2>

  <ul class="abs services-list">
    <li>Physiatrists</li>
    <li>Sport Medicine</li>
    <li>Physicians</li>
    <li>Physiotherapists</li>
    <li>Chiropractors</li>
    <li>Massage Therapists</li>
    <li>Acupuncturists</li>
    <li>Psychologists</li>
  </ul>

  <div class="abs wave-band waves-inside" role="img" aria-label="Soft green flowing wave decoration"></div>

  <p class="abs services-note">We provide integrated assessment and care from interprofessional team of regulated healthcare professionals with proven experience in injury rehabilitation.</p>

  <p class="abs promise-lead">We provide custom medical bracing, orthotics, orthopedic shoes, assistive devices, and medical stockings, all in one place.</p>
  <h3 class="abs promise-head" style="top:161px">Registered physiotherapists</h3>
  <p class="abs promise-body" style="top:201px">We strongly believe in consistency with your treatment plan. This means that you spend your time here one-on-one with your physiotherapist, not any students or assistants. You get consistent high quality care from a professional.</p>
  <h3 class="abs promise-head" style="top:322px">One-on-one attention</h3>
  <p class="abs promise-body" style="top:362px">We book maximum 3 people per hour to ensure everyone gets adequate one-on-one time with their physiotherapist. This compares favorably with other clinics, who may book upwards of 5-6 per hour. The atmosphere is professional -balanced with friendly, caring and relaxed. Our highly qualified staff operate this way to help make your recovery faster and more enjoyable.</p>
</section>

</body>
</html>
```